tidal box

TIDAL BOX mobile technology servicesPhone and tablet repairs, screens data recovery.

Industry/Entity Type

Data Recovery

Contact Information for Business Card

0491 573 086

Colors
33a6d7
f04a50
0a90cc
e34197

Requirements
Must have
• Liam hardy
Nice to have
• White background

```html
<!DOCTYPE html>
<html lang="en">
<head>
<meta charset="UTF-8">
<title>Tidal Box – Business Card</title>
<link href="https://fonts.googleapis.com/css2?family=Open+Sans:wght@300;600;700;800&display=swap" rel="stylesheet">
<style>
  :root {
    --orange: #f39325;
    --orange-deep: #ec8421;
    --grey: #6d6e71;
    --white: #ffffff;
    --soft-white: #fbefe2;
    --font: "Open Sans", Arial, sans-serif;
  }
  * { margin: 0; padding: 0; box-sizing: border-box; }
  html, body {
    width: 1200px; height: 741px; overflow: hidden;
    background: var(--white);
    font-family: var(--font);
  }
  .card {
    position: relative;
    width: 1200px; height: 741px;
    background: var(--white);
    overflow: hidden;
  }
  .side-band {
    position: absolute; left: 19px; top: 19px;
    width: 208px; height: 702px;
    background: linear-gradient(160deg, var(--orange), var(--orange-deep));
  }
  .device-art {
    position: absolute; left: 104px; top: 182px;
    width: 196px; height: 350px;
    border-radius: 30px;
    background: linear-gradient(160deg, #f2f2f2 0%, #d9d9d9 100%);
    transform: rotate(-27deg);
    box-shadow: 6px 4px 0 var(--orange-deep);
  }
  .tagline {
    position: absolute; right: 627px; top: 60px;
    text-align: right;
    color: var(--grey);
    font-weight: 600; font-size: 30px; line-height: 40px;
  }
  .brand-name {
    position: absolute; right: 627px; top: 158px;
    text-align: right;
    color: var(--orange);
    font-weight: 800; font-size: 140px; line-height: 144px;
    letter-spacing: -3px;
  }
  .services {
    position: absolute; right: 627px; top: 526px;
    text-align: right;
    font-weight: 600; font-size: 29px; line-height: 40px;
    color: var(--grey);
  }
  .services .service-group + .service-group { margin-top: 16px; }
  .services .service-key {
    display: block;
    color: var(--orange);
    font-weight: 800;
    letter-spacing: 1px;
  }
  .info-panel {
    position: absolute; left: 598px; top: 19px;
    width: 583px; height: 702px;
    background: linear-gradient(160deg, var(--orange), var(--orange-deep));
    color: var(--white);
  }
  .person-name {
    position: absolute; left: 80px; top: 62px;
    font-weight: 700; font-size: 80px; line-height: 90px;
    letter-spacing: -0.5px;
  }
  .person-role {
    position: absolute; left: 80px; top: 138px;
    font-weight: 300; font-size: 74px; line-height: 84px;
  }
  .contact-list { list-style: none; }
  .contact-item {
    position: absolute; left: 38px;
    display: flex; align-items: flex-start;
    color: var(--soft-white);
    font-weight: 600; font-size: 39px; line-height: 47px;
  }
  .contact-item .icon {
    width: 50px; flex: none;
    display: flex; justify-content: center;
    margin-right: 33px;
  }
  .contact-address { top: 300px; }
  .contact-address .icon { padding-top: 6px; }
  .contact-phone { top: 414px; }
  .contact-phone .icon { padding-top: 2px; }
  .contact-email { top: 540px; }
  .contact-email .icon { padding-top: 10px; }
  .contact-web { top: 610px; }
  .contact-web .icon { padding-top: 3px; }
</style>
</head>
<body>
  <div class="card">
    <div class="side-band"></div>
    <div class="device-art" role="img" aria-label="Illustration of a smartphone with a cracked screen"></div>

    <p class="tagline">mobile technology<br>services</p>
    <h1 class="brand-name">TIDAL<br>BOX</h1>

    <div class="services">
      <p class="service-group">Phone and tablet<span class="service-key">REPAIRS</span></p>
      <p class="service-group">Screens data<span class="service-key">RECOVERY</span></p>
    </div>

    <section class="info-panel">
      <h2 class="person-name">Liam Hardy</h2>
      <p class="person-role">Director</p>

      <ul class="contact-list">
        <li class="contact-item contact-address">
          <span class="icon">
            <svg width="34" height="62" viewBox="0 0 34 62" aria-hidden="true">
              <path d="M17 0C7.6 0 0 7.6 0 17c0 12 17 45 17 45s17-33 17-45C34 7.6 26.4 0 17 0z" fill="#fbefe2"/>
              <circle cx="17" cy="17" r="7" fill="#f08a23"/>
            </svg>
          </span>
          <span>48 Harbour Lane<br>Bayford, 20417</span>
        </li>
        <li class="contact-item contact-phone">
          <span class="icon">
            <svg width="36" height="46" viewBox="0 0 36 46" aria-hidden="true">
              <path d="M9 1l6 10c1 2 0 3-1 4l-4 3c1 6 6 14 12 17l4-3c1-1 3-1 4 0l6 9c1 2 0 3-1 4-3 2-7 3-10 1C13 40 3 25 2 12 1 8 3 4 6 1c1-1 2-1 3 0z" fill="#fbefe2"/>
            </svg>
          </span>
          <span>0491 573 086</span>
        </li>
        <li class="contact-item contact-email">
          <span class="icon">
            <svg width="50" height="32" viewBox="0 0 50 32" aria-hidden="true">
              <rect x="0" y="0" width="50" height="32" fill="#fbefe2"/>
              <path d="M1 1l24 17L49 1" fill="none" stroke="#f08a23" stroke-width="2.5"/>
            </svg>
          </span>
          <span>repair@tidalbox.co</span>
        </li>
        <li class="contact-item contact-web">
          <span class="icon">
            <svg width="46" height="46" viewBox="0 0 46 46" aria-hidden="true">
              <rect x="0" y="0" width="46" height="46" rx="3" fill="#fbefe2"/>
            </svg>
          </span>
          <span>www.tidalbox.co</span>
        </li>
      </ul>
    </section>
  </div>
</body>
</html>
```